Study Lantern

StudyLantern.com will be a place for people looking for information, resources, and advisement to start or continue their education. We want a friendly, inviting site design that makes finding what potential students are looking for simple and easy to navigate. We are not committed to the colors of the logo, so variations on the color scheme are welcome.

Text instructions based on the wireframe: For the site's homepage we'd like a banner at the very top for our Logo and white space to the right of it. See attachments for logo + wireframe. Below that would be navigation. Below that split into 2/3 on the left we would have home page content, and 1/3 on the right we would have the lead form. At the bottom of the page we would have a space for types of degrees, then a footer with copyright info + site info.

See wireframes for additional page layouts.

Industry/Entity Type

Education

Requirements
Must have
• At minimum we are looking for three pages: homepage, choose your degree path page, and content page.
Nice to have
• -White space is appreciated
-Variations on the color scheme are welcome, we are not married to the existing logo's color scheme.

```html
<!DOCTYPE html>
<html lang="en">
<head>
<meta charset="utf-8">
<title>Study Lantern — Home</title>
<link href="https://fonts.googleapis.com/css2?family=Questrial&family=Arimo:wght@400;700&display=swap" rel="stylesheet">
<style>
:root{
  --gold:#f0b000;
  --gold-dark:#d99a00;
  --ink:#4a4a4a;
  --text:#5a5a5a;
  --charcoal:#3c3c3c;
  --cream:#f3f2e8;
  --field:#e4e4e4;
  --footer:#3d3d3d;
  --footer-text:#b8b8b8;
  --navy:#1d3a66;
}
*{box-sizing:border-box;margin:0;padding:0}
html,body{width:932px;height:1200px;overflow:hidden}
body{position:relative;background:linear-gradient(90deg,#d9d9d9 0%,#f4f4f4 8%,#f4f4f4 92%,#d9d9d9 100%);font-family:"Arimo",Arial,sans-serif;color:var(--text)}
.abs{position:absolute}
.header{left:0;top:0;width:932px;height:94px;background:linear-gradient(#fff,#ececec)}
.brand{left:78px;top:38px;font-family:"Questrial",sans-serif;font-size:31px;color:var(--ink);display:flex;align-items:center;gap:10px}
.brand .mark{width:22px;height:22px;background:var(--gold)}
.follow{left:724px;top:11px;font-size:8.5px;font-weight:700;color:#666;display:flex;align-items:center;gap:5px}
.follow span.sq{width:14px;height:14px;background:#555;border-radius:2px}
.call-icon{left:683px;top:36px;width:50px;height:50px;border-radius:4px;background:#fff;box-shadow:0 1px 3px rgba(0,0,0,.3);display:flex;align-items:center;justify-content:center}
.call-icon div{width:40px;height:40px;background:var(--gold);border-radius:3px;display:flex;align-items:center;justify-content:center}
.call-text{left:739px;top:45px;font-family:"Questrial",sans-serif;color:var(--navy);font-size:12.5px;line-height:15px}
.call-text b{display:block;font-family:"Arimo",sans-serif;color:var(--charcoal);font-size:16px}
.stage{left:60px;top:94px;width:812px;height:1013px;background:var(--cream)}
.nav{left:28px;top:105px;width:877px;height:40px}
.nav-links{left:298px;top:95px;height:43px;display:flex;font-family:"Questrial",sans-serif;font-size:11.5px;letter-spacing:.4px;color:#3a3a3a}
.nav-links a{color:inherit;text-decoration:none;display:flex;align-items:center;padding:0 21px;height:43px;padding-top:10px;border-left:1px dashed #8a6a10}
.nav-links a.active{background:var(--charcoal);color:#fff;border:none;width:80px;justify-content:center}
.nav-links a.active+a{border-left:none}
.slider{left:72px;top:150px;width:786px;height:322px;background:#f3f3f3;border:1px solid #ddd;box-shadow:0 1px 3px rgba(0,0,0,.15)}
.slide{left:81px;top:159px;width:769px;height:283px;background:linear-gradient(90deg,#6f7a55 0%,#c7c9b4 40%,#d9dccb 70%,#b5b9a1 100%)}
.dots{left:424px;top:449px;display:flex;gap:5px}
.dots i{width:16px;height:16px;border-radius:50%;background:#a5a5a5}
.dots i:first-child{background:var(--charcoal)}
.shelf{left:85px;top:472px;width:760px;height:24px}
h2.section{font-family:"Questrial",sans-serif;font-weight:400;color:var(--ink)}
h2.section em{font-style:normal;color:var(--gold)}
.rule{height:3px;background:linear-gradient(90deg,#bbb,rgba(0,0,0,0))}
.welcome-icon{left:94px;top:509px;width:38px;height:52px;background:#777;border-radius:5px;color:#eee;font-size:5.5px;display:flex;align-items:center;justify-content:center;font-family:"Arimo",sans-serif}
.copy{font-size:10.2px;line-height:14.6px;text-align:justify;color:#555}
.btn{background:#333;color:#fff;font-size:9px;border-radius:3px;padding:4px 5px;display:inline-block}
.divider{left:591px;top:510px;width:1px;height:432px;background:#bbb}
.lead-icon{left:612px;top:508px;width:38px;height:40px;background:linear-gradient(#aaa,#777);border-radius:4px}
.field{left:614px;width:217px;height:21px;background:var(--field);border:1px solid #ececec;font-size:10px;color:#444;padding:4px 6px}
.submit{left:614px;top:783px;width:61px;height:19px;background:#222;color:#fff;font-size:10px;font-weight:700;border-radius:3px;text-align:center;line-height:19px}
.or{left:707px;top:777px;font-family:"Questrial",sans-serif;font-size:37px;color:#ddd;font-weight:700}
.callnow{left:608px;top:828px;width:238px;height:108px;background:#fff;border:1px solid #ddd}
.handset{left:0;top:0;width:80px;height:106px;background:linear-gradient(135deg,#f2d8c4,#e86a2a 60%,#fff)}
.degrees{left:82px;top:982px;width:766px;height:106px;background:#ececec;border:1px solid #fff;border-radius:5px;box-shadow:0 0 0 1px #d8d8d8}
.cert{top:12px;width:97px;height:73px;border:3px solid}
.footer{left:0;top:1107px;width:932px;height:93px;background:var(--footer);color:var(--footer-text);font-size:10px}
.foot-brand{left:72px;top:40px;font-family:"Questrial",sans-serif;font-size:24px;color:#ddd;display:flex;align-items:center;gap:8px}
.foot-brand .mark{width:18px;height:18px;background:#999}
.foot-links{left:290px;top:31px;width:380px;text-align:center;line-height:17px}
.foot-address{right:76px;top:14px;text-align:right;line-height:16.2px}
</style>
</head>
<body>
<header class="header abs">
  <div class="brand abs"><span>Study Lantern</span><span class="mark"></span></div>
  <div class="follow abs">Follow Us on : <span class="sq"></span><span class="sq"></span><span class="sq"></span></div>
  <div class="call-icon abs"><div>
    <svg width="18" height="24" viewBox="0 0 18 24"><rect x="1" y="1" width="16" height="22" rx="2" fill="#fff"/><rect x="4" y="4" width="10" height="6" fill="#f0b000"/><g fill="#f0b000"><rect x="4" y="13" width="2" height="2"/><rect x="8" y="13" width="2" height="2"/><rect x="12" y="13" width="2" height="2"/><rect x="4" y="17" width="2" height="2"/><rect x="8" y="17" width="2" height="2"/><rect x="12" y="17" width="2" height="2"/></g></svg>
  </div></div>
  <div class="call-text abs">CALL US TOLL-FREE<b>555 .014 .2280</b></div>
</header>

<div class="stage abs"></div>

<svg class="nav abs" viewBox="0 0 877 40" preserveAspectRatio="none">
  <polygon points="0,6 28,6 28,50 0,50 10,28" fill="#e3a200"/>
  <polygon points="877,6 849,6 849,50 877,50 867,28" fill="#e3a200"/>
  <defs><linearGradient id="band" x1="0" y1="0" x2="0" y2="1"><stop offset="0" stop-color="#fcc418"/><stop offset="1" stop-color="#e7a800"/></linearGradient></defs>
  <rect x="21" y="0" width="835" height="40" fill="url(#band)"/>
</svg>
<nav class="nav-links abs">
  <a class="active" href="#">HOME</a><a href="#">ABOUT US</a><a href="#">SERVICES</a><a href="#">DEGREES</a><a href="#">FAQ’S</a><a href="#">CONTACT US</a>
</nav>

<div class="slider abs"></div>
<div class="slide abs" role="img" aria-label="Smiling student with a backpack on a sunny campus lawn, classmates in the background"></div>
<div class="dots abs"><i></i><i></i><i></i><i></i><i></i></div>
<svg class="shelf abs" viewBox="0 0 760 24" preserveAspectRatio="none"><defs><linearGradient id="sh" x1="0" y1="0" x2="0" y2="1"><stop offset="0" stop-color="#cfcfc6"/><stop offset="1" stop-color="#f3f2e8"/></linearGradient></defs><polygon points="0,24 60,0 700,0 760,24" fill="url(#sh)"/></svg>

<div class="welcome-icon abs">WELCOME</div>
<h2 class="section abs" style="left:143px;top:524px;font-size:26px">Welcome - <em>degree guidance</em></h2>
<div class="rule abs" style="left:143px;top:559px;width:160px"></div>
<p class="copy abs" style="left:88px;top:572px;width:478px">Curabitur mattis sem tincidunt arcu gravida aliquet. In hac habitasse platea dictumst. Class aptent taciti sociosqu ad litora torquent per conubia nostra, per inceptos himenaeos. Quisque nisi risus, varius et sodales vitae, imperdiet vel sapien. In et est a elit luctus lacinia eu vel sapien. Mauris pulvinar venenatis elit nec egestas.</p>
<p class="copy abs" style="left:88px;top:645px;width:478px">Proin hendrerit euismod velit, non imperdiet dolor aliquam et. Nullam id nulla vitae sem congue ultrices eu id sapien. Donec et dolor ac dui suscipit pellentesque. Pellentesque habitant morbi tristique senectus et netus et malesuada fames ac turpis egestas. Nunc at velit sapien. Aenean iaculis odio quis lacus bibendum volutpat lobortis libero tincidunt. Nullam ut risus turpis. In nulla tellus, semper ut ornare et, adipiscing sed arcu.</p>
<span class="btn abs" style="left:507px;top:724px">Read more ▸</span>

<svg class="abs" style="left:92px;top:764px" width="34" height="48" viewBox="0 0 34 48"><text x="2" y="34" font-family="Arimo,sans-serif" font-weight="700" font-size="40" fill="#888">?</text></svg>
<h2 class="section abs" style="left:130px;top:777px;font-size:15.5px">Why <em>choose us ??</em></h2>
<div class="rule abs" style="left:131px;top:803px;width:190px"></div>
<p class="copy abs" style="left:88px;top:820px;width:478px">Pellentesque habitant morbi tristique senectus et netus et malesuada fames ac turpis egestas. Nunc at velit sapien. Aenean iaculis odio quis lacus bibendum volutpat lobortis libero tincidunt. Nullam ut risus turpis. In nulla tellus, semper ut ornare et, adipiscing sed arcu.<br>Quisque nisi risus, varius et sodales vitae, imperdiet vel sapien. In et est a elit luctus lacinia eu vel sapien. Mauris pulvinar venenatis elit nec egestas.</p>
<span class="btn abs" style="left:507px;top:907px">Read more ▸</span>

<div class="divider abs"></div>

<div class="lead-icon abs"></div>
<h2 class="section abs" style="left:657px;top:516px;font-size:16px">Lead <em>Form</em></h2>
<div class="rule abs" style="left:657px;top:537px;width:100px;height:2px"></div>
<p class="abs" style="left:615px;top:554px;width:212px;font-size:10px;line-height:14.5px;color:#666">Send us a quick email with any questions or concerns you may have about your potential case.</p>
<div class="field abs" style="top:601px">Your Name</div>
<div class="field abs" style="top:629px">Your Email Address</div>
<div class="field abs" style="top:656px">Your Phone No.</div>
<div class="field abs" style="top:683px;display:flex;justify-content:space-between">Interested In <span style="font-size:7px;padding-top:2px">▼</span></div>
<div class="field abs" style="top:710px;height:59px">Provide Your Education Details.</div>
<div class="submit abs">Submit</div>
<div class="or abs">OR</div>
<div class="callnow abs">
  <div class="handset abs" role="img" aria-label="Hand holding an orange telephone handset"></div>
  <div class="abs" style="left:90px;top:2px;font-family:Arimo,sans-serif;font-weight:700;font-size:40px;color:var(--gold);line-height:46px">CLICK</div>
  <div class="abs" style="left:96px;top:44px;font-weight:700;font-size:14px;letter-spacing:1px;color:#222">CALL-US-NOW</div>
  <div class="abs" style="left:80px;top:65px;font-size:9px;line-height:13px;color:#222">Have a question about your career ?<br>Click here to connect to our office.</div>
  <div class="abs" style="left:80px;top:92px;font-weight:700;font-size:19px;color:#333;letter-spacing:.5px">555 .014 .2280</div>
</div>

<h2 class="section abs" style="left:122px;top:948px;font-size:15.5px">List of <em>degrees</em></h2>
<div class="rule abs" style="left:122px;top:972px;width:100px"></div>
<div class="degrees abs">
  <div class="cert abs" role="img" aria-label="Certificate" style="left:18px;border-color:#6b3a4a;background:#efe7d4"></div>
  <div class="cert abs" role="img" aria-label="Certificate" style="left:140px;border-color:#f5ebd0;background:#f7f0dc"></div>
  <div class="cert abs" role="img" aria-label="Certificate" style="left:263px;border-color:#8aa6d6;background:#fafafa"></div>
  <div class="cert abs" role="img" aria-label="Certificate" style="left:385px;border-color:#d5a27a;background:#fbf6ee"></div>
  <div class="cert abs" role="img" aria-label="Certificate" style="left:510px;border-color:#555;background:#ebebeb"></div>
  <div class="cert abs" role="img" aria-label="Certificate" style="left:635px;border-color:#9a9a9a;background:#fafafa"></div>
</div>

<footer class="footer abs">
  <div class="foot-brand abs"><span>Study Lantern</span><span class="mark"></span></div>
  <div class="foot-links abs">Home &nbsp; | &nbsp; About Us &nbsp; | &nbsp; Services &nbsp; | &nbsp; Degrees &nbsp; | &nbsp; FAQs &nbsp; | &nbsp; Contact<br>Copyright © 2011 - studylantern - All rights reserved. Terms and Privacy Policy</div>
  <div class="foot-address abs"><b>Address Line 1 with City</b><br><b>Address Line 2 with Country</b><br>Tel. : 555 . 014 . 2280<br>Email : info@studylantern.com</div>
</footer>
</body>
</html>
```